Ridgeway Truck & Bus Center, Truck Repair, Light.medium duty trucks

May an eye catching banner for Truck & Bus Repair to be used on Facebook, Possibly printable banner.

Target Market(s)

Need to target Fleet's or walk in customers for Light, Medium and Heavy Duty Truck and Bus Repairs

Industry/Entity Type

Truck Repair

Other font styles liked:
• Please see my sample uploaded

Requirements
Must have
• Some visually appealing, Use of logo, a modern look and feel to design. Would like market towards medium duty and heavy duty truck repair clientele.
Nice to have
• If can get logos of vehicle makes which can be seen in my sample I uploaded. Please add kelbro mfg logo as I’m a warranty ac repair facility, as well as please refer to all other make logos in my sample
Uploaded would I.e. varn, Dastorene, Pelloway,Brin,voltan etc please see sample for all other logo makes.

```html
<!DOCTYPE html>
<html lang="en">
<head>
<meta charset="utf-8">
<title>Ridgeway Truck &amp; Bus Center – Repair Banner</title>
<link href="https://fonts.googleapis.com/css2?family=Saira+Condensed:wght@600;700;800&display=swap" rel="stylesheet">
<style>
  :root {
    --page: #dcdcdc;
    --red: #a3101c;
    --red-deep: #6e0710;
    --red-dark: #3c0308;
    --black: #141414;
    --white: #ffffff;
    --silver: #d9d9d9;
    --grey-light: #eeeeee;
    --grey-mid: #b9b9b9;
  }
  * { box-sizing: border-box; margin: 0; padding: 0; }
  html, body {
    width: 1200px; height: 537px; overflow: hidden;
    background: var(--page);
    font-family: "Saira Condensed", "Arial Narrow", sans-serif;
  }
  .banner {
    position: absolute; left: 0; top: 49px;
    width: 1200px; height: 439px; overflow: hidden;
    background: var(--red);
  }
  .banner-bg { position: absolute; inset: 0; }
  .headline-top, .headline-main, .tagline, .services, .contact, .brand-bar, .client-mark {
    position: absolute;
  }
  .headline-top {
    left: 526px; top: 30px; width: 545px;
    font-size: 31px; font-weight: 800; line-height: 1; letter-spacing: 0.2px;
    color: var(--silver); text-shadow: 2px 2px 2px rgba(0,0,0,.55);
    white-space: nowrap;
  }
  .headline-main {
    left: 524px; top: 58px; width: 548px;
    font-size: 66px; font-weight: 800; line-height: 1; letter-spacing: 0.5px;
    color: var(--silver); text-shadow: 3px 3px 3px rgba(0,0,0,.55);
    white-space: nowrap;
  }
  .tagline {
    left: 526px; top: 122px; width: 543px; height: 30px;
    background: var(--black);
    clip-path: polygon(8px 0, 100% 0, calc(100% - 8px) 100%, 0 100%);
    color: var(--silver); font-size: 17.5px; font-weight: 700;
    line-height: 30px; text-align: center; white-space: nowrap;
  }
  .services {
    left: 532px; top: 170px; width: 520px;
    display: grid; grid-template-columns: 226px 280px; row-gap: 4px;
    list-style: none;
  }
  .service {
    display: flex; align-items: center; gap: 9px; height: 24px;
    color: var(--white); font-size: 22px; font-weight: 700; white-space: nowrap;
  }
  .service svg { width: 19px; height: 19px; flex: none; }
  .contact { left: 532px; top: 309px; color: var(--white); }
  .contact-row { display: flex; align-items: center; gap: 26px; height: 26px; }
  .contact-item {
    display: flex; align-items: center; gap: 8px;
    font-size: 21px; font-weight: 700; white-space: nowrap;
  }
  .contact-item svg { width: 15px; height: 17px; flex: none; }
  .brand-bar {
    left: 0; top: 382px; width: 1200px; height: 57px;
    background: var(--black);
    display: flex; align-items: center; justify-content: space-between;
    padding: 0 230px 0 14px;
  }
  .brand {
    color: var(--grey-mid); font-size: 12.5px; font-weight: 700;
    letter-spacing: 0.3px; text-transform: uppercase; white-space: nowrap;
  }
  .client-mark {
    left: 1021px; top: 271px; width: 190px; height: 190px;
    border-radius: 50%;
    background: var(--black);
    border: 4px solid var(--grey-light);
    display: flex; flex-direction: column; align-items: center; justify-content: center;
    padding-right: 14px; padding-top: 10px;
  }
  .client-name {
    color: var(--white); font-size: 31px; font-weight: 800; line-height: 1; letter-spacing: 1px;
  }
  .client-sub {
    color: var(--white); font-size: 10px; font-weight: 700; letter-spacing: 2.4px; margin-top: 4px;
  }
</style>
</head>
<body>
<main class="banner">
  <svg class="banner-bg" viewBox="0 0 1200 439" width="1200" height="439" aria-hidden="false">
    <defs>
      <linearGradient id="redField" x1="0" y1="0" x2="1" y2="0">
        <stop offset="0" stop-color="#b01220"/>
        <stop offset="0.6" stop-color="#8e0b16"/>
        <stop offset="1" stop-color="#3c0308"/>
      </linearGradient>
      <linearGradient id="workshopTone" x1="0" y1="0" x2="1" y2="0">
        <stop offset="0" stop-color="#c9c9c9"/>
        <stop offset="1" stop-color="#f2f2f2"/>
      </linearGradient>
      <radialGradient id="truckTone" cx="0.55" cy="0.55" r="0.6">
        <stop offset="0" stop-color="#c8232c"/>
        <stop offset="0.6" stop-color="#8f1a20"/>
        <stop offset="1" stop-color="#9a9a9a" stop-opacity="0.5"/>
      </radialGradient>
      <radialGradient id="glovesTone" cx="0.5" cy="0.5" r="0.5">
        <stop offset="0" stop-color="#7a0a14" stop-opacity="0.9"/>
        <stop offset="1" stop-color="#7a0a14" stop-opacity="0"/>
      </radialGradient>
    </defs>
    <rect width="1200" height="439" fill="url(#redField)"/>
    <rect role="img" aria-label="Mechanic's gloved hands with a wrench, faint red-toned photo" x="860" y="150" width="340" height="230" fill="url(#glovesTone)"/>
    <path d="M0 0 H415 Q515 210 392 382 H0 Z" fill="#ffffff" opacity="0.9"/>
    <path role="img" aria-label="Workshop background photo in pale grey" d="M0 0 H395 Q480 210 370 382 H0 Z" fill="url(#workshopTone)"/>
    <rect role="img" aria-label="Photo of a red heavy-duty semi truck with silver box trailer" x="40" y="44" width="432" height="338" rx="24" fill="url(#truckTone)"/>
  </svg>

  <h1 class="headline-top">COMPREHENSIVE MEDIUM AND HEAVY DUTY REPAIR</h1>
  <h2 class="headline-main">TRUCK AND BUS REPAIRS</h2>
  <p class="tagline">WE ARE EQUIPPED TO HANDLE EVEN THE TOUGHEST HEAVY DUTY REPAIR PROJECTS.</p>

  <ul class="services">
    <li class="service"><svg viewBox="0 0 20 20"><circle cx="10" cy="10" r="6.5" fill="none" stroke="#d9d9d9" stroke-width="3" stroke-dasharray="3 2"/><circle cx="10" cy="10" r="2.5" fill="#d9d9d9"/></svg>HYDRAULIC REPAIRS</li>
    <li class="service"><svg viewBox="0 0 20 20"><circle cx="10" cy="10" r="6.5" fill="none" stroke="#d9d9d9" stroke-width="3" stroke-dasharray="3 2"/><circle cx="10" cy="10" r="2.5" fill="#d9d9d9"/></svg>FULL ECM PROGRAMMING</li>
    <li class="service"><svg viewBox="0 0 20 20"><circle cx="10" cy="10" r="6.5" fill="none" stroke="#d9d9d9" stroke-width="3" stroke-dasharray="3 2"/><circle cx="10" cy="10" r="2.5" fill="#d9d9d9"/></svg>LIFT GATE REPAIRS</li>
    <li class="service"><svg viewBox="0 0 20 20"><circle cx="10" cy="10" r="6.5" fill="none" stroke="#d9d9d9" stroke-width="3" stroke-dasharray="3 2"/><circle cx="10" cy="10" r="2.5" fill="#d9d9d9"/></svg>PREVENTIVE MAINTENANCE</li>
    <li class="service"><svg viewBox="0 0 20 20"><circle cx="10" cy="10" r="6.5" fill="none" stroke="#d9d9d9" stroke-width="3" stroke-dasharray="3 2"/><circle cx="10" cy="10" r="2.5" fill="#d9d9d9"/></svg>FULL AC REPAIRS</li>
    <li class="service"><svg viewBox="0 0 20 20"><circle cx="10" cy="10" r="6.5" fill="none" stroke="#d9d9d9" stroke-width="3" stroke-dasharray="3 2"/><circle cx="10" cy="10" r="2.5" fill="#d9d9d9"/></svg>SUSPENSION REPAIRS</li>
    <li class="service"><svg viewBox="0 0 20 20"><circle cx="10" cy="10" r="6.5" fill="none" stroke="#d9d9d9" stroke-width="3" stroke-dasharray="3 2"/><circle cx="10" cy="10" r="2.5" fill="#d9d9d9"/></svg>INFRAME REBUILDS</li>
    <li class="service"><svg viewBox="0 0 20 20"><circle cx="10" cy="10" r="6.5" fill="none" stroke="#d9d9d9" stroke-width="3" stroke-dasharray="3 2"/><circle cx="10" cy="10" r="2.5" fill="#d9d9d9"/></svg>MUCH MORE...</li>
  </ul>

  <div class="contact">
    <div class="contact-row">
      <span class="contact-item"><svg viewBox="0 0 16 16"><rect width="16" height="16" rx="3" fill="#141414"/><path d="M4.5 3.5l2 2-1 1.3c.6 1.4 1.7 2.5 3.1 3.1l1.3-1 2 2-1.2 1.6C7.4 11.9 4.1 8.6 3.5 5.3z" fill="#c8102e"/></svg>5715550142</span>
      <span class="contact-item"><svg viewBox="0 0 16 16"><rect width="16" height="16" rx="3" fill="#141414"/><path d="M4.5 3.5l2 2-1 1.3c.6 1.4 1.7 2.5 3.1 3.1l1.3-1 2 2-1.2 1.6C7.4 11.9 4.1 8.6 3.5 5.3z" fill="#c8102e"/></svg>5715550187</span>
    </div>
    <div class="contact-row">
      <span class="contact-item"><svg viewBox="0 0 14 18"><path d="M7 0a6 6 0 0 0-6 6c0 4.5 6 12 6 12s6-7.5 6-12a6 6 0 0 0-6-6z" fill="#141414"/><circle cx="7" cy="6" r="2.2" fill="#a3101c"/></svg>4210 ASHGROVE PL &nbsp;#4 MILLBRIDGE &nbsp;VA 22090</span>
    </div>
  </div>

  <div class="brand-bar">
    <span class="brand">Varn</span>
    <span class="brand">Dastorene</span>
    <span class="brand">Corvane</span>
    <span class="brand">Tarrok</span>
    <span class="brand">Hesko</span>
    <span class="brand">Brin</span>
    <span class="brand">Stellmark</span>
    <span class="brand">Ozumi</span>
    <span class="brand">Kendrall</span>
    <span class="brand">Norcoach</span>
    <span class="brand">Veldhaus</span>
    <span class="brand">Sprintline</span>
    <span class="brand">Astorin</span>
    <span class="brand">Udara</span>
    <span class="brand">Pelloway</span>
    <span class="brand">Petrick</span>
    <span class="brand">Voltan</span>
    <span class="brand">Dalmont</span>
    <span class="brand">Kelbro</span>
  </div>

  <div class="client-mark">
    <span class="client-name">RIDGEWAY</span>
    <span class="client-sub">TRUCK &amp; BUS CENTER</span>
  </div>
</main>
</body>
</html>
```